Business Card for By Karel Voss

Looking to have a business card designed for my lifestyle and fitness company. My company offers personal training, online programming and nutrition advice based out of London, United Kingdom.

I'd like to see modern, sleek designs, focusing on black, matte black or matte grey. Design doesn't need to be overly descriptive as this will also be used as a personal business card. I've included my logo.

Please note that my company is no longer called "Fitness by Karel Voss" but instead "By Karel Voss", this is because of my other ventures. Therefore please don't use the "fitness by karel voss" text.

information about my company can be found at www.bykarelvoss.com

Company is also based out of London (United Kingdom) & Sydney (Australia) this could be reflected on the card.

Industry/Entity Type

Business

Contact Information for Business Card

Karel Voss
+44 7382 615027
karel@bykarelvoss.com
www.bykarelvoss.com

Font styles to use
Sans Serif

Requirements
Must have
• All contact details and inclusion of my logo.

```html
<!DOCTYPE html>
<html lang="en">
<head>
<meta charset="utf-8">
<title>By Karel Voss – Business Card</title>
<link rel="stylesheet" href="https://fonts.googleapis.com/css2?family=Exo+2:wght@400;700&display=swap">
<style>
  :root {
    --backdrop: #111111;
    --card: #2a2a2b;
    --ink: #f2f2f2;
    --ink-soft: #d6d6d6;
  }
  * { box-sizing: border-box; margin: 0; padding: 0; }
  html, body {
    width: 1200px;
    height: 1000px;
    overflow: hidden;
    background: var(--backdrop);
    font-family: "Exo 2", "Helvetica Neue", Arial, sans-serif;
    color: var(--ink);
  }
  .stage {
    position: relative;
    width: 1200px;
    height: 1000px;
  }
  .card {
    position: absolute;
    top: 357px;
    width: 500px;
    height: 286px;
    background: var(--card);
    border-radius: 2px;
  }
  .card--front { left: 60px; }
  .card--back { left: 640px; }

  /* Front */
  .brand-mark {
    position: absolute;
    inset: 0;
    display: flex;
    align-items: center;
    justify-content: center;
    gap: 14px;
  }
  .brand-mark__dot {
    width: 30px;
    height: 30px;
    border-radius: 50%;
    background: var(--ink);
  }
  .brand-mark__name {
    font-weight: 700;
    font-size: 26px;
    letter-spacing: 0.08em;
    text-transform: uppercase;
    color: var(--ink);
  }

  /* Back */
  .holder-name {
    position: absolute;
    left: 32px;
    top: 30px;
    font-size: 22px;
    font-weight: 700;
    letter-spacing: 0.02em;
  }
  .contact {
    position: absolute;
    left: 32px;
    top: 96px;
    list-style: none;
    font-size: 13px;
    line-height: 1.5;
    color: var(--ink-soft);
  }
  .social {
    position: absolute;
    left: 32px;
    top: 168px;
    display: flex;
    gap: 8px;
  }
  .social__item {
    width: 24px;
    height: 24px;
    border: 1.5px solid var(--ink);
    border-radius: 50%;
  }
  .bar-rule {
    position: absolute;
    left: 140px;
    top: 172px;
  }
  .logo-slot {
    position: absolute;
    right: 30px;
    top: 110px;
    display: flex;
    align-items: center;
    gap: 10px;
  }
  .logo-slot__dot {
    width: 20px;
    height: 20px;
    border-radius: 50%;
    background: var(--ink);
  }
  .logo-slot__name {
    font-weight: 700;
    font-size: 20px;
    letter-spacing: 0.06em;
    text-transform: uppercase;
  }
  .website {
    position: absolute;
    right: 30px;
    bottom: 26px;
    font-size: 16px;
    letter-spacing: 0.03em;
  }
</style>
</head>
<body>
<main class="stage">
  <section class="card card--front" aria-label="Card front">
    <div class="brand-mark">
      <span class="brand-mark__dot"></span>
      <span class="brand-mark__name">By Karel Voss</span>
    </div>
  </section>

  <section class="card card--back" aria-label="Card back">
    <h1 class="holder-name">Karel Voss</h1>
    <ul class="contact">
      <li>+44 7382 615027</li>
      <li>karel@bykarelvoss.com</li>
    </ul>
    <div class="social" aria-label="Social profiles">
      <span class="social__item"></span>
      <span class="social__item"></span>
      <span class="social__item"></span>
    </div>
    <svg class="bar-rule" width="150" height="16" viewBox="0 0 150 16" aria-hidden="true">
      <line x1="0" y1="8" x2="150" y2="8" stroke="#f2f2f2" stroke-width="1.5"/>
      <rect x="12" y="3" width="2" height="10" fill="#f2f2f2"/>
      <rect x="136" y="3" width="2" height="10" fill="#f2f2f2"/>
    </svg>
    <div class="logo-slot">
      <span class="logo-slot__dot"></span>
      <span class="logo-slot__name">By Karel Voss</span>
    </div>
    <p class="website">www.ByKarelVoss.com</p>
  </section>
</main>
</body>
</html>
```